Bramble Harbor Foundation Web Design

The design we need is for a WordPress blog that will be our content platform. We are a registered 501(c)3 non-profit that focuses on financially supporting the treatment of cancer patients that have been told they have no hope and there is nothing the conventional medical system can do for them. Through this wesbite we want to both rasie awareness about the treatment options plus, raise funds for treating patients. The two primary target audiences of the site are...

1. Terminally ill patients and their families to let them know that there is an option other then hospice and that we are hear to support that option.

2. People looking to help donate to a worthwhile cause that resonates with them.

The website is https://brambleharborfoundation.org/

See attached logo designs!!!

Target Market(s)

Cancer patients and their families

Industry/Entity Type

Foundation

Font styles to use
Sans Serif

Colors
ffffff
fbed22

Requirements
Must have
• I like this look of this site. It is clean, simple, helpful, soft. I like the flow of the pages.
• http://www.quietmeadowtrust.org/
• I like the design and flow but NOT the color or boldness
• https://tmvq-youth.org/
• I like this style for a donation page.
• https://www.curewaveaid.org/about-cwa/stand-with-us/gifts/single-gift
• with the addition of a Would you like your employer to match? button.
Nice to have
• White black and gold - but soft
• Even possibly grayscale like the site I like.

```html
<!DOCTYPE html>
<html lang="en">
<head>
<meta charset="utf-8">
<title>Bramble Harbor Foundation</title>
<link href="https://fonts.googleapis.com/css2?family=Lato:wght@300;400;700&display=swap" rel="stylesheet">
<style>
  :root {
    --white: #ffffff;
    --ink: #4a4a4a;
    --ink-soft: #8a8a8a;
    --pink: #fbb0da;
    --gold: #f1cc5c;
    --footer-bg: #e8e8e8;
    --hero-a: #cdbdbb;
    --hero-b: #b9a7a4;
  }
  * { box-sizing: border-box; margin: 0; padding: 0; }
  html, body { width: 1200px; height: 2562px; overflow: hidden; background: var(--white); }
  body { position: relative; font-family: 'Lato', sans-serif; color: var(--ink); }
  .abs { position: absolute; }

  .site-header { left: 0; top: 0; width: 1200px; height: 87px; background: var(--white); border-bottom: 1px solid #ececec; }
  .brand { left: 128px; top: 28px; display: flex; align-items: center; gap: 8px; font-size: 14px; font-weight: 700; color: var(--ink); }
  .brand-dot { width: 16px; height: 16px; border-radius: 50%; background: var(--gold); }
  .main-nav { left: 518px; top: 34px; display: flex; gap: 0; font-size: 14px; font-weight: 300; color: var(--ink-soft); }
  .main-nav span { position: absolute; white-space: nowrap; }

  .btn { position: absolute; border-radius: 5px; color: var(--white); font-size: 13px; font-weight: 700; display: flex; align-items: center; justify-content: center; }
  .btn-pink { background: var(--pink); }
  .btn-gold { background: var(--gold); }

  .hero { left: 0; top: 87px; width: 1200px; height: 504px; background: linear-gradient(100deg, var(--hero-a), var(--hero-b) 50%, #d6c9c7); }
  .hero-title { left: 0; width: 1190px; top: 214px; text-align: center; font-size: 27px; color: var(--white); }
  .hero-sub { left: 0; width: 1190px; top: 256px; text-align: center; font-size: 17px; color: var(--white); }
  .hero-label { top: 330px; width: 300px; text-align: center; font-size: 18px; color: var(--white); }

  .section-title { font-size: 27px; font-weight: 400; color: var(--ink); }
  .body-text { font-size: 14px; font-weight: 300; color: var(--ink-soft); line-height: 32px; }

  .about-title { left: 0; width: 1190px; top: 672px; text-align: center; }
  .about-text { left: 280px; width: 630px; top: 743px; text-align: center; }

  .photo { position: absolute; border-radius: 7px; }
  .stat { position: absolute; width: 220px; text-align: center; }
  .stat-num { font-size: 34px; font-weight: 700; color: var(--ink); line-height: 1; }
  .stat-label { font-size: 13px; font-weight: 300; color: var(--ink-soft); margin-top: 8px; }

  .site-footer { left: 0; top: 2377px; width: 1200px; height: 185px; background: var(--footer-bg); }
  .foot-head { font-size: 15px; font-weight: 300; color: var(--ink-soft); }
  .foot-link { font-size: 12px; font-weight: 300; color: var(--ink-soft); line-height: 19px; }
  .social { left: 604px; top: 2468px; display: flex; gap: 15px; }
  .social span { width: 20px; height: 20px; border-radius: 50%; background: #9a9a9a; }
</style>
</head>
<body>

<header class="abs site-header">
  <div class="abs brand"><span class="brand-dot"></span>Bramble Harbor Foundation</div>
  <nav class="abs main-nav">
    <span style="left:0">Home</span>
    <span style="left:72px">About</span>
    <span style="left:143px">How it Works</span>
    <span style="left:260px">News</span>
    <span style="left:321px">Contact us</span>
  </nav>
  <a class="btn btn-pink" style="left:940px;top:27px;width:123px;height:33px;font-weight:400">Donate</a>
</header>

<section class="abs hero" role="img" aria-label="Photo of a woman in a headscarf embraced by a young girl, soft pink tones"></section>
<h1 class="abs hero-title" style="font-weight:400">Together We Can Beat a Cancer</h1>
<p class="abs hero-sub">Just a few simple steps, and someones life can be saved</p>
<p class="abs hero-label" style="left:224px">For mecenats</p>
<a class="btn btn-pink" style="left:287px;top:371px;width:176px;height:32px">Donate</a>
<p class="abs hero-label" style="left:664px">For cancer patients</p>
<a class="btn btn-gold" style="left:728px;top:371px;width:176px;height:32px">Learn more</a>

<h2 class="abs section-title about-title">About Us</h2>
<p class="abs body-text about-text">We are a registered 501(c)3 non-profit that focuses on financially supporting the research and treatment of cancer patients that have been told they have no hope and there is nothing the conventional medical system can do for them.</p>
<a class="btn btn-gold" style="left:508px;top:877px;width:176px;height:32px">Learn more</a>

<div class="photo" style="left:0;top:998px;width:349px;height:400px;background:linear-gradient(135deg,#6e7a5c,#e8c9c0 55%,#f3a8c4);border-radius:0 7px 7px 0" role="img" aria-label="Photo of two smiling women outdoors"></div>
<div class="photo" style="left:366px;top:998px;width:381px;height:400px;background:linear-gradient(180deg,#e9ddc6,#d89a7a 55%,#8e8a5a)" role="img" aria-label="Photo of a smiling woman in a red headscarf"></div>
<div class="photo" style="left:764px;top:998px;width:320px;height:400px;background:linear-gradient(160deg,#dd3f95,#4f6f36 60%,#e9c2b4)" role="img" aria-label="Photo of a young child in a pink headscarf"></div>
<div class="photo" style="left:1102px;top:998px;width:98px;height:400px;background:linear-gradient(180deg,#f3ddd6,#e7b3c0);border-radius:7px 0 0 7px" role="img" aria-label="Photo with soft pink flowers"></div>

<div class="stat" style="left:128px;top:1480px"><div class="stat-num">2700</div><div class="stat-label">Lorem ipsum dolor set</div></div>
<div class="stat" style="left:367px;top:1480px"><div class="stat-num">2700</div><div class="stat-label">Lorem ipsum dolor set</div></div>
<div class="stat" style="left:604px;top:1480px"><div class="stat-num">2700</div><div class="stat-label">Lorem ipsum dolor set</div></div>
<div class="stat" style="left:844px;top:1480px"><div class="stat-num">2700</div><div class="stat-label">Lorem ipsum dolor set</div></div>

<div class="photo" style="left:0;top:1627px;width:508px;height:309px;background:linear-gradient(120deg,#cfc3ad,#9c8a78 45%,#2f8f96);border-radius:0 7px 7px 0" role="img" aria-label="Photo of a smiling child hugging a doll"></div>
<h2 class="abs section-title" style="left:605px;top:1660px">For Mecenats</h2>
<p class="abs body-text" style="left:605px;top:1710px;width:440px">Lorem ipsum dolor sit amet, consectetur adipiscing elit, sed do eiusmod tempor incididunt ut labore et dolore magna aliqua. Ut enim ad minim veniam, quis nostrud exercitation ullamco laboris nisi ut aliquip ex ea commodo consequat.</p>
<a class="btn btn-pink" style="left:605px;top:1861px;width:176px;height:33px">Donate</a>

<h2 class="abs section-title" style="left:128px;top:2014px">For Cancer Patients</h2>
<p class="abs body-text" style="left:128px;top:2065px;width:440px">Lorem ipsum dolor sit amet, consectetur adipiscing elit, sed do eiusmod tempor incididunt ut labore et dolore magna aliqua. Ut enim ad minim veniam, quis nostrud exercitation ullamco laboris nisi ut aliquip ex ea commodo consequat.</p>
<a class="btn btn-gold" style="left:128px;top:2215px;width:176px;height:32px">Learn more</a>
<div class="photo" style="left:684px;top:1981px;width:516px;height:309px;background:linear-gradient(110deg,#d9cfc4,#6fb3c4 35%,#e6c3b2 65%,#a9a9a9);border-radius:7px 0 0 7px" role="img" aria-label="Photo of a woman hugging a patient in a blue headscarf"></div>

<footer class="abs site-footer"></footer>
<p class="abs foot-head" style="left:128px;top:2434px">Bramble Harbor Foundation</p>
<p class="abs foot-link" style="left:128px;top:2465px">Privacy policy<br>Terms and conditions</p>
<p class="abs foot-head" style="left:366px;top:2434px">Contact us</p>
<p class="abs foot-link" style="left:366px;top:2465px">hello@brambleharbor.org<br>+33 1 00 48 27 19</p>
<p class="abs foot-head" style="left:603px;top:2434px">Follow us</p>
<div class="abs social"><span></span><span></span><span></span></div>
<a class="btn btn-pink" style="left:885px;top:2440px;width:178px;height:33px">Contact us</a>

</body>
</html>
```